Cover Design Brief – Prayer Book (Modern Revision)

Design a new, modern, high-quality book cover that reflects the essence of the original version. The updated cover should feel contemporary yet familiar, appealing to both younger and older readers, while evoking a sense of spiritual depth, calm, and authenticity.

1. Visual Reference to the Original Cover
Continuity:
Retain visual elements such as the color palette, central motifs (eg, geometric patterns, Islamic ornaments, or a symbolic figure), and overall structure from the original cover.

Recognition:
Readers familiar with the old cover should instantly recognize the book but be pleasantly surprised by the refined, modern look.

2. Style & Mood
Modern Islamic design, minimalist and clean rather than ornate.

Spiritual, calming, elegant – avoid overly bright or flashy visuals.

Subtle use of Islamic motifs, possibly a decorative Arabic calligraphy word like ṣalāh (صلاة) to enrich the theme.

3. Suggested Color Palette
Deep blue, teal, petrol green, olive, sand tones, or midnight blue with accents of gold – depending on the original cover scheme.

Avoid neon or loud colors.

If gold or silver is used, it should be subtle and classy (eg, foil stamping or embossing, not digital effects).

4. Typography
A modern serif font for the main title is welcome, but it should be clean and elegant.

Subtitles should use a clear, legible font.

If the title includes Arabic text, it should be displayed in tasteful classical calligraphy or a stylized script.

5. Back Cover
Will include a brief description text (to be provided later).

Clean layout, optionally with a small publisher logo.

Possibly a short quote or ḥadīth in Arabic (with or without translation) to complement the design.

6. Target Audience
German-speaking Muslims, male and female, ages 15+

Suitable for both beginners and advanced practitioners of the prayer

Designed as a long-term spiritual companion and a thoughtful gift

```html
<!DOCTYPE html>
<html lang="de">
<head>
<meta charset="utf-8">
<title>Aṣ-Ṣalāh – Das Gebet im Islam · Cover</title>
<link rel="stylesheet" href="https://fonts.googleapis.com/css2?family=Noto+Serif:wght@400;500;600;700&display=swap">
<style>
  :root {
    --page: #ffffff;
    --gold: #f7c04f;
    --ink-light: #ffffff;
    --petrol: #2c4650;
    --photo-top: #d3dadd;
    --photo-mid: #7e9199;
    --photo-low: #2d4a53;
    --photo-deep: #12303a;
    --seal: #25434c;
  }
  * { box-sizing: border-box; margin: 0; padding: 0; }
  html, body { width: 900px; height: 1200px; overflow: hidden; background: var(--page); }
  body { position: relative; font-family: "Noto Serif", Georgia, serif; }

  .front-cover {
    position: absolute; width: 442px; height: 628px; overflow: hidden;
    text-align: center; color: var(--ink-light);
  }
  .front-cover--single { left: 223px; top: 35px; box-shadow: -14px 16px 26px rgba(0,0,0,.28); }
  .front-cover--wrap { left: 460px; top: 711px; transform: scale(.711); transform-origin: 0 0; }

  .cover-photo {
    position: absolute; inset: 0;
    background:
      radial-gradient(ellipse 40% 45% at 50% 22%, rgba(255,255,255,.55), transparent 70%),
      linear-gradient(180deg, var(--photo-top) 0%, #aab7bc 38%, var(--photo-mid) 48%, var(--photo-low) 70%, var(--photo-deep) 100%);
  }
  .cover-title {
    position: absolute; left: 0; right: 0; top: 228px;
    font-size: 68px; font-weight: 600; color: var(--gold); line-height: 1;
    letter-spacing: .5px; text-shadow: 0 2px 3px rgba(0,0,0,.25);
  }
  .calligraphy-seal {
    position: absolute; left: 174px; top: 332px; width: 94px; height: 94px;
  }
  .cover-subtitle {
    position: absolute; left: 0; right: 0; top: 424px; line-height: 1;
  }
  .cover-subtitle .main { display: block; font-size: 40px; font-weight: 500; }
  .cover-subtitle .sub { display: block; font-size: 31px; font-weight: 500; margin-top: 2px; }
  .edition-note {
    position: absolute; left: 0; right: 0; top: 515px;
    font-size: 19px; line-height: 28px; color: var(--gold); font-weight: 500;
  }
  .publisher-line {
    position: absolute; left: 0; right: 0; top: 584px; font-size: 14.5px; letter-spacing: .3px;
  }

  .book-wrap { position: absolute; left: 115px; top: 711px; width: 345px; height: 446px; background: var(--petrol); }
  .back-cover-heading {
    position: absolute; left: 214px; top: 771px; font-size: 17px; font-weight: 600;
    color: var(--gold); line-height: 1.3; white-space: nowrap;
  }
  .back-seal { position: absolute; left: 306px; top: 767px; width: 34px; height: 34px; }
  .back-publisher {
    position: absolute; left: 136px; top: 1128px; width: 60px; text-align: center;
    font-size: 7px; color: var(--gold); line-height: 1.2;
  }
  .spine-title {
    position: absolute; left: 443px; top: 936px; white-space: nowrap;
    font-size: 14px; color: var(--gold); font-weight: 500; line-height: 1;
    transform: translate(-50%, -50%) rotate(-90deg);
  }
  .spine-publisher {
    position: absolute; left: 431px; top: 1090px; width: 26px; text-align: center;
    font-size: 5px; color: var(--gold); line-height: 1.2;
  }
</style>
</head>
<body>

  <section class="front-cover front-cover--single">
    <div class="cover-photo" role="img" aria-label="Lichtdurchfluteter Moscheeinnenraum mit weißer Gebetsnische und Minbar über Gebetsteppichreihen"></div>
    <h1 class="cover-title">Aṣ-Ṣalāh</h1>
    <svg class="calligraphy-seal" viewBox="0 0 94 94" role="img" aria-label="Arabische Kalligrafie des Wortes as-Salah im Kreis">
      <circle cx="47" cy="47" r="45" fill="var(--seal)" stroke="#fff" stroke-width="2"/>
      <circle cx="47" cy="47" r="41" fill="none" stroke="#fff" stroke-width="1"/>
    </svg>
    <p class="cover-subtitle"><span class="main">Das Gebet</span><span class="sub">im Islam</span></p>
    <p class="edition-note">Vollstadig<br>revidierte Ausgabe</p>
    <p class="publisher-line">Nurhaus Verlag</p>
  </section>

  <div class="book-wrap"></div>
  <p class="back-cover-heading">Aṣ-Ṣalāh</p>
  <svg class="back-seal" viewBox="0 0 34 34" role="img" aria-label="Arabische Kalligrafie des Wortes as-Salah im Kreis">
    <circle cx="17" cy="17" r="16" fill="var(--seal)" stroke="#fff" stroke-width="1"/>
    <circle cx="17" cy="17" r="13.5" fill="none" stroke="#fff" stroke-width=".6"/>
  </svg>
  <p class="back-publisher">Nurhaus Verlag</p>
  <p class="spine-title">Aṣ-Ṣalāh - Das Gebet im Islam</p>
  <p class="spine-publisher">Nurhaus Verlag</p>

  <section class="front-cover front-cover--wrap">
    <div class="cover-photo" role="img" aria-label="Lichtdurchfluteter Moscheeinnenraum mit weißer Gebetsnische und Minbar über Gebetsteppichreihen"></div>
    <h2 class="cover-title">Aṣ-Ṣalāh</h2>
    <svg class="calligraphy-seal" viewBox="0 0 94 94" role="img" aria-label="Arabische Kalligrafie des Wortes as-Salah im Kreis">
      <circle cx="47" cy="47" r="45" fill="var(--seal)" stroke="#fff" stroke-width="2"/>
      <circle cx="47" cy="47" r="41" fill="none" stroke="#fff" stroke-width="1"/>
    </svg>
    <p class="cover-subtitle"><span class="main">Das Gebet</span><span class="sub">im Islam</span></p>
    <p class="edition-note">Vollstadig<br>revidierte Ausgabe</p>
    <p class="publisher-line">Nurhaus Verlag</p>
  </section>

</body>
</html>
```